Employee I.D. Card - Badge

We need an employee I.D. card designed. Our employees are going to be wearing these. I would like to have it look nice. Something professional yet cool (not uptight if that makes sense).
Project Scope:
Vertical orientation
Company name ------------- (Bright and Tidy)
Website ------------- (brightandtidymn.example)
Employee Picture
background check image
front and back designed - same design on either side
You can create the card without having the employee images on them.
Here are the dimensions -
2.125 x 3.370 inches
Double sided - same design can be used front and back
Background badge - I would like to add an image that shows that the employee has taken a background check. I've added the press-kit for the company we use. If you have a better idea than incorporating their logo, we can certainly do something different.
Example image-
https://www.lookupzone.example/find?q=background+check+badge&kind=images&ref=XyZ4qWm82LpRt:
The print company will set up the names.
Logo is attached
Also attached are our business cards. You can use this for an idea of brand/company style.
Our website - brightandtidymn.example

```html
<!DOCTYPE html>
<html lang="en">
<head>
<meta charset="utf-8">
<title>Bright and Tidy — Employee I.D. Card</title>
<link href="https://fonts.googleapis.com/css2?family=Roboto:wght@300;400&display=swap" rel="stylesheet">
<style>
  :root {
    --backdrop: #d9dadb;
    --card: #efefef;
    --card-edge: #e2e2e2;
    --brand-blue: #1b86d0;
    --text-grey: #555555;
    --photo-bg: #a9a9a9;
    --photo-shade: #8c8c8c;
    --badge-ring: #3b3b3b;
    --badge-green: #7cc242;
    --pattern-light: #f2f2f2;
    --pattern-tone: #e6e6e6;
  }
  * { box-sizing: border-box; margin: 0; padding: 0; }
  html, body {
    width: 1200px;
    height: 1108px;
    overflow: hidden;
  }
  body {
    background: var(--backdrop);
    font-family: "Roboto", Arial, sans-serif;
    position: relative;
  }
  .id-card {
    position: absolute;
    top: 237px;
    width: 400px;
    height: 634px;
    background: var(--card);
    border: 1px solid var(--card-edge);
    border-radius: 24px;
    box-shadow: 0 10px 28px rgba(0, 0, 0, 0.18);
    overflow: hidden;
  }
  .id-card--front { left: 170px; }
  .id-card--back { left: 630px; }

  .brand-name {
    font-weight: 300;
    color: var(--brand-blue);
    font-size: 58px;
    line-height: 1.02;
    letter-spacing: -1px;
    display: flex;
    align-items: center;
    gap: 14px;
  }
  .brand-name__dot {
    width: 16px;
    height: 16px;
    border-radius: 50%;
    background: var(--brand-blue);
    flex: none;
  }

  .id-card--front .brand-name {
    position: absolute;
    top: 70px;
    left: 72px;
  }
  .website {
    position: absolute;
    top: 222px;
    left: 0;
    width: 100%;
    text-align: center;
    font-size: 19px;
    color: var(--text-grey);
    letter-spacing: 0.2px;
  }
  .employee-photo {
    position: absolute;
    top: 290px;
    left: 120px;
    width: 160px;
    height: 172px;
    border-radius: 12px;
    border: 3px solid #ffffff;
    background: linear-gradient(180deg, var(--photo-bg), var(--photo-shade));
  }
  .check-badge {
    position: absolute;
    top: 415px;
    left: 74px;
    width: 128px;
    height: 128px;
  }

  .back-pattern {
    position: absolute;
    inset: 0 0 200px 0;
    background: linear-gradient(170deg, var(--pattern-tone), var(--pattern-light));
  }
  .id-card--back .brand-name {
    position: absolute;
    bottom: 70px;
    left: 72px;
  }
</style>
</head>
<body>

  <section class="id-card id-card--front" aria-label="Employee card, front">
    <div class="brand-name">
      <span class="brand-name__dot"></span>
      <span>Bright<br>and Tidy</span>
    </div>
    <p class="website">www.brightandtidymn.example</p>
    <div class="employee-photo" role="img" aria-label="Employee photo placeholder"></div>
    <svg class="check-badge" viewBox="0 0 128 128" role="img" aria-label="Background check cleared badge">
      <circle cx="64" cy="64" r="62" fill="var(--badge-green)"/>
      <circle cx="64" cy="64" r="52" fill="var(--badge-ring)"/>
      <circle cx="64" cy="64" r="20" fill="var(--badge-green)"/>
    </svg>
  </section>

  <section class="id-card id-card--back" aria-label="Employee card, back">
    <div class="back-pattern" role="img" aria-label="Faint repeating brand-name background pattern"></div>
    <div class="brand-name">
      <span class="brand-name__dot"></span>
      <span>Bright<br>and Tidy</span>
    </div>
  </section>

</body>
</html>
```